Business card design for a engineering company

I need a double sided business card design for my company "Velbrook Stream Systems". The card will be used in Malaysia. Sleek and professional, with a little design flare to it.
Information to showcase:
1. Company logo
2. Name, title, phone, email address, website address
3. our products "Pumping technology, Valve & actuation, Air Moving Technology
Example:
Mark Dovan
Business manager
mark.dovan@velbrook-example.com
www.velbrook-example.com.my
- Pumping technology
- Valve & actuation
- Air moving technology
Target Market(s)
engineers, purchasing managers
Industry/Entity Type
Business
Contact Information for Business Card
Mark Dovan
Business manager
mark.dovan@velbrook-example.com
www.velbrook-example.com.my
- Pumping technology
- Valve & actuation
- Air moving technology
catch phrase : "Solving flow challenges, exceeding expectations"

```html
<!DOCTYPE html>
<html lang="en">
<head>
<meta charset="utf-8">
<title>Velbrook Stream Systems – Business Card</title>
<link rel="stylesheet" href="https://fonts.googleapis.com/css2?family=Arimo:wght@400;700&display=swap">
<style>
  :root{
    --backdrop:#3a3a3a;
    --navy:#17303d;
    --navy-light:#22414f;
    --orange:#e8822a;
    --orange-deep:#d8692c;
    --amber:#e39a2a;
    --ink:#2b2b2b;
    --paper:#f7f7f7;
    --paper-shade:#e9e9e9;
  }
  *{margin:0;padding:0;box-sizing:border-box;}
  html,body{width:1200px;height:965px;overflow:hidden;}
  body{background:var(--backdrop);font-family:"Arimo",Arial,sans-serif;position:relative;}
  .card{position:absolute;left:246px;width:710px;height:404px;border-radius:36px;overflow:hidden;}
  .card-front{top:60px;background:radial-gradient(circle at 45% 45%,#ffffff 0%,var(--paper) 50%,var(--paper-shade) 100%);}
  .card-back{top:504px;background:linear-gradient(180deg,var(--navy-light) 0%,var(--navy) 100%);}

  .brand{position:absolute;display:flex;align-items:center;gap:14px;font-weight:700;letter-spacing:1px;}
  .brand-dot{display:block;border-radius:50%;flex:none;}
  .card-front .brand{left:46px;top:62px;color:var(--navy);font-size:30px;}
  .card-front .brand-dot{width:60px;height:60px;background:var(--orange);}
  .card-back .brand{left:0;right:0;top:160px;justify-content:center;color:#ffffff;font-size:38px;}
  .card-back .brand-dot{width:76px;height:76px;background:var(--orange);}

  .contact{position:absolute;left:442px;top:168px;color:var(--ink);}
  .contact-name{font-size:22px;font-weight:400;color:#10222c;line-height:26px;}
  .contact-title{font-size:16px;color:var(--orange);line-height:20px;}
  .contact-list{list-style:none;margin-top:16px;}
  .contact-list li{display:flex;align-items:center;gap:8px;font-size:15px;line-height:20px;}
  .contact-list svg{width:16px;height:16px;flex:none;}
  .contact-address{margin-top:18px;font-size:15px;line-height:20px;}

  .front-band{position:absolute;left:0;right:0;bottom:0;height:28px;display:flex;}
  .front-band .band-warm{flex:none;width:460px;background:linear-gradient(90deg,var(--orange-deep),var(--amber));}
  .front-band .band-gap{flex:none;width:4px;background:#ffffff;}
  .front-band .band-navy{flex:none;width:60px;background:var(--navy);}
  .front-band .band-end{flex:1;background:var(--amber);}

  .product-band{position:absolute;left:0;right:0;top:328px;height:48px;background:linear-gradient(180deg,var(--amber),var(--orange-deep));display:flex;align-items:center;justify-content:center;gap:14px;color:#fff5e6;font-size:17px;}
  .product-band .divider{opacity:.9;}
</style>
</head>
<body>
  <section class="card card-front">
    <div class="brand"><span class="brand-dot"></span>VELBROOK STREAM SYSTEMS</div>

    <div class="contact">
      <p class="contact-name">Mark Dovan</p>
      <p class="contact-title">Business manager</p>
      <ul class="contact-list">
        <li>
          <svg viewBox="0 0 16 16"><path fill="#e8822a" d="M3 1.5l2.5-.5 1.5 3.5-1.7 1.2a8 8 0 0 0 4.9 4.9l1.2-1.7 3.5 1.5-.5 2.5c-.3.9-1 1.3-2 1.1C7 12.9 3.1 9 1.9 3.5c-.2-1 .2-1.7 1.1-2z"/></svg>
          +60 3 7842 5516
        </li>
        <li>
          <svg viewBox="0 0 16 16"><rect x="1" y="3" width="14" height="10" fill="#e8822a"/><path d="M1 3l7 6 7-6" fill="none" stroke="#fff" stroke-width="1.4"/></svg>
          mark.dovan@velbrook-example.com
        </li>
        <li>
          <svg viewBox="0 0 16 16" fill="none" stroke="#e8822a" stroke-width="1.3"><circle cx="8" cy="8" r="6.5"/><ellipse cx="8" cy="8" rx="3" ry="6.5"/><path d="M1.5 8h13M2.5 4.8h11M2.5 11.2h11"/></svg>
          www.velbrook-example.com.my
        </li>
      </ul>
      <p class="contact-address">Here your company or<br>home address</p>
    </div>

    <div class="front-band">
      <span class="band-warm"></span><span class="band-gap"></span><span class="band-navy"></span><span class="band-gap"></span><span class="band-end"></span>
    </div>
  </section>

  <section class="card card-back">
    <div class="brand"><span class="brand-dot"></span>VELBROOK STREAM SYSTEMS</div>
    <div class="product-band">
      <span>Pumping technology</span><span class="divider">|</span>
      <span>Valve &amp; actuation</span><span class="divider">|</span>
      <span>Air moving technology</span>
    </div>
  </section>
</body>
</html>
```